23rd Annual Harrowgate Lantern Film Festival Poster

Design an eye catchy, stylish poster for our 23rd film festival. Be different not just a poster with a film reel. Think outside of the box with a design that will attract peoples attention. Colorful (you choose the colors). Make it fun and creative, like the film festival. Show your talents in the design. Be sure it is new and stylish. Dates are August 21 - 29, 2020. Poster size will be 27 inches by 40 inches

Target Market(s)

Upper Middle class - movie lovers

Font styles to use
Sans Serif

Colors
33a6d7

Requirements
Must have
• NO CLIP ART - be original !
Nice to have
• abstract - think outside the box
Should not have
• CLIP ART

```html
<!DOCTYPE html>
<html lang="en">
<head>
<meta charset="utf-8">
<title>Harrowgate Lantern Film Festival – 23rd Poster</title>
<link rel="stylesheet" href="https://fonts.googleapis.com/css2?family=Lexend:wght@600;700&family=Montserrat:wght@300;800&display=swap">
<style>
  :root {
    --backdrop: #f1f1f1;
    --poster-blue: #2f4fa4;
    --ray: #33a6d7;
    --title-gold: #e9b523;
    --badge-pink: #e0449a;
    --badge-lime: #b8d63c;
    --white: #ffffff;
    --figure-dark: #16204a;
    --figure-light: #e4e6ea;
  }
  html, body {
    margin: 0;
    width: 1200px;
    height: 1200px;
    overflow: hidden;
    background: var(--backdrop);
  }
  .poster {
    position: absolute;
    left: 222px;
    top: 40px;
    width: 756px;
    height: 1120px;
    background: var(--poster-blue);
    overflow: hidden;
    font-family: "Lexend", sans-serif;
  }
  .key-art {
    position: absolute;
    left: 52px;
    top: 0;
    width: 704px;
    height: 770px;
    background:
      linear-gradient(100deg,
        rgba(51, 166, 215, 0.35) 0%,
        var(--ray) 38%,
        var(--figure-dark) 62%,
        var(--figure-dark) 70%,
        var(--figure-light) 90%);
  }
  .date-block {
    position: absolute;
    left: 40px;
    top: 292px;
    width: 256px;
    transform: rotate(-90deg);
    transform-origin: top left;
    color: var(--white);
    white-space: nowrap;
  }
  .date-block .festival-mark {
    display: block;
    font-family: "Montserrat", sans-serif;
    font-weight: 800;
    font-size: 92px;
    line-height: 78px;
    letter-spacing: 1px;
  }
  .date-block .month,
  .date-block .days {
    display: block;
    font-family: "Montserrat", sans-serif;
    font-weight: 300;
    font-size: 92px;
    line-height: 66px;
    color: transparent;
    -webkit-text-stroke: 2px var(--white);
  }
  .title {
    position: absolute;
    left: 0;
    top: 782px;
    margin: 0;
    color: var(--title-gold);
    font-weight: 600;
    font-size: 72px;
    line-height: 77px;
    letter-spacing: 1px;
  }
  .title span { display: block; }
  .title .flush { padding-left: 72px; }
  .title .indent { padding-left: 133px; }
  .edition {
    position: absolute;
    left: 472px;
    top: 918px;
    color: var(--badge-pink);
    -webkit-text-stroke: 3px var(--badge-lime);
    font-weight: 700;
    white-space: nowrap;
  }
  .edition .number { font-size: 156px; letter-spacing: -10px; }
  .edition .suffix {
    font-size: 70px;
    vertical-align: 62px;
    margin-left: 8px;
  }
</style>
</head>
<body>
  <main class="poster">
    <div class="key-art" role="img" aria-label="Illustration of projector light beams fanning toward a stylised woman with a dark bob haircut, 3D glasses and red lips"></div>

    <div class="date-block">
      <span class="festival-mark">LUMA</span>
      <span class="month">aug</span>
      <span class="days">21-29</span>
    </div>

    <h1 class="title">
      <span class="flush">HARROWGATE</span>
      <span class="indent">LANTERN</span>
      <span class="indent">FILM</span>
      <span class="flush">FESTIVAL</span>
    </h1>

    <div class="edition"><span class="number">23</span><span class="suffix">rd</span></div>
  </main>
</body>
</html>
```